Pack design: Meal Kits for older consumers - VIVORA

Pack design for a new to market Meal Kit specifically designed for the older consumer (over 65)

VIVORA - small bites of food for BIG BITES OF LIFE
fortified and nutritious small portion meals for older consumers.

Target Market(s)

Over 65 year olds

Industry/Entity Type

Food Production

Font styles to use
Sans Serif

Colors
6b449b
b768aa
b7a5cd
ffffff
e4daeb
ecdaeb

Requirements
Must have
• Pack design that is appealing to the 0ver 65s but MUST not be patronising.
• Large easy to read font
Nice to have
• Logo
• Instructions inside pack

```html
<!DOCTYPE html>
<html lang="en">
<head>
<meta charset="utf-8">
<title>VIVORA – Meal Kit Pack</title>
<link href="https://fonts.googleapis.com/css2?family=Oswald:wght@400;500&family=Open+Sans:ital,wght@0,700;1,800&display=swap" rel="stylesheet">
<style>
  :root {
    --purple-deep: #6b449b;
    --purple-mid: #b768aa;
    --lavender: #b7a5cd;
    --mist: #e4daeb;
    --blush: #ecdaeb;
    --white: #ffffff;
    --kraft: #b48a57;
    --kraft-dark: #a57c4b;
    --backdrop: #e6e6e6;
    --ink: #3a2a3f;
  }
  * { box-sizing: border-box; margin: 0; padding: 0; }
  html, body { width: 1200px; height: 900px; overflow: hidden; }
  body { background: var(--backdrop); position: relative; }

  .pack-front {
    position: absolute; left: 100px; top: 172px;
    width: 1000px; height: 555px;
    background: linear-gradient(180deg, var(--kraft) 0%, var(--kraft-dark) 100%);
  }

  .sleeve {
    position: absolute; left: 228px; top: 0;
    width: 517px; height: 555px;
    border-left: 12px solid var(--lavender);
    border-right: 12px solid var(--lavender);
    overflow: hidden;
  }
  .sleeve-photo {
    position: absolute; inset: 0;
    background:
      radial-gradient(ellipse at 62% 58%, #c7915a 0%, #b9875c 25%, transparent 55%),
      radial-gradient(ellipse at 40% 60%, #e8dccb 0%, #d9c8b2 40%, transparent 70%),
      linear-gradient(180deg, #3b3a40 0%, #8f8a88 28%, #d8d2cc 55%, #efebe7 100%);
  }

  .brand-top {
    position: absolute; top: 48px; left: 0; right: 0;
    text-align: center;
    font-family: 'Oswald', sans-serif; font-weight: 500;
    font-size: 30px; letter-spacing: 2px; color: var(--purple-deep);
  }
  .tagline-ribbon {
    position: absolute; top: 100px; left: 30px; width: 433px; height: 44px;
  }
  .tagline-ribbon svg { position: absolute; inset: 0; }
  .tagline-text {
    position: absolute; inset: 0;
    display: flex; align-items: center; justify-content: center;
    font-family: 'Oswald', sans-serif; font-weight: 500;
    font-size: 17px; letter-spacing: 0.3px; color: var(--purple-mid);
    text-transform: uppercase;
  }

  .brand-seal {
    position: absolute; top: 248px; left: 50%;
    transform: translateX(-50%);
    width: 100px; height: 100px; border-radius: 50%;
    background: var(--white);
    display: flex; align-items: center; justify-content: center;
    font-family: 'Oswald', sans-serif; font-weight: 500;
    font-size: 26px; letter-spacing: 1px; color: var(--purple-deep);
  }

  .info-panel {
    position: absolute; left: 12px; right: 12px; top: 368px;
    height: 162px;
    background: var(--white);
    padding: 6px;
  }
  .info-frame {
    border: 3px solid var(--lavender);
    height: 100%;
    padding: 6px 14px 0 22px;
    position: relative;
  }
  .product-title {
    font-family: 'Open Sans', sans-serif; font-weight: 800; font-style: italic;
    font-size: 17px; color: var(--purple-mid); text-align: center;
    margin-bottom: 4px;
  }
  .benefit-list {
    list-style: disc; padding-left: 22px;
    font-family: 'Oswald', sans-serif; font-weight: 400;
    font-size: 10.5px; line-height: 14.5px; color: var(--ink);
    text-transform: uppercase;
  }
  .eco-icons {
    position: absolute; right: 14px; bottom: 10px;
    display: flex; gap: 8px;
  }
</style>
</head>
<body>
  <div class="pack-front">
    <div class="sleeve">
      <div class="sleeve-photo" role="img" aria-label="Photo of a bowl of ramen noodles in creamy broth with glazed tofu, a soft-boiled egg and spring onions, hand holding chopsticks"></div>

      <div class="brand-top">VIVORA</div>

      <div class="tagline-ribbon">
        <svg viewBox="0 0 433 44" width="433" height="44" aria-hidden="true">
          <polygon points="0,14 26,10 26,40 0,42 10,28" fill="#e4daeb"/>
          <polygon points="433,14 407,10 407,40 433,42 423,28" fill="#e4daeb"/>
          <path d="M20 6 Q216 -6 413 6 L413 36 Q216 24 20 36 Z" fill="#ffffff" stroke="#b7a5cd" stroke-width="1.5"/>
        </svg>
        <div class="tagline-text">Small bites of food for big bites of life</div>
      </div>

      <div class="brand-seal">VIVORA</div>

      <div class="info-panel">
        <div class="info-frame">
          <h2 class="product-title">Japanese Ramen Broths with fresh vegetables</h2>
          <ul class="benefit-list">
            <li>Specially designed for the older consumer</li>
            <li>Fortified with protein and calcium to maintain muscle mass and bone health</li>
            <li>A small portions to suit older appetites</li>
            <li>All the nutrients you need in small but mighty portions</li>
            <li>Easy to use and the directions are easy to follow</li>
            <li>Leave no waste</li>
            <li>Packaging is all recyclable or biodegradable</li>
          </ul>
          <div class="eco-icons" aria-hidden="true">
            <svg width="16" height="18" viewBox="0 0 16 18">
              <rect x="2" y="4" width="12" height="13" rx="1" fill="#8fbf6a"/>
              <rect x="0" y="2" width="16" height="2" fill="#8fbf6a"/>
              <rect x="6" y="0" width="4" height="2" fill="#8fbf6a"/>
            </svg>
            <svg width="18" height="18" viewBox="0 0 18 18">
              <path d="M9 2 L14 10 M14 10 L4 10 M4 10 L9 2" stroke="#8fbf6a" stroke-width="2" fill="none"/>
              <circle cx="9" cy="10" r="7" stroke="#8fbf6a" stroke-width="1" fill="none"/>
            </svg>
          </div>
        </div>
      </div>
    </div>
  </div>
</body>
</html>
```